Sales pitch for "Brimvale Surplus Co"

We need a new sales pitch deck (and company logo) for our new company "Brimvale Surplus Co". We collect surplus foods & goods and resell them at a discounted price to end-customers and businesses.
Show why / mission of what we do is important (combat global warming, etc.), what our concept is, who we are, why they should join / what we look for,
The story-line and content can be found in the attached Powerpoint file.
Target Market(s)
Food manufacturers, retailers, distributors, wholesale
Industry/Entity Type
Food & beverages
Requirements
Must have
- Editable PowerPoint (16:9), use storyline in attached file. You may split or combine slides, shorten / edit content, use new imagery, etc.
Nice to have
- Professional, clean, sustainable, fresh, ...
Should not have
- Funny, comics / cartoons, ...

```html
<!DOCTYPE html>
<html lang="en">
<head>
<meta charset="utf-8">
<title>Brimvale Surplus Co – Team</title>
<link rel="stylesheet" href="https://fonts.googleapis.com/css2?family=Arimo:ital,wght@0,400;0,700;1,400&family=Poppins:wght@600&display=swap">
<style>
  :root {
    --sky-top: #62d3ef;
    --sky-bottom: #2581bd;
    --card-top: rgba(20, 70, 140, 0);
    --card-bottom: #0c2b5e;
    --white: #ffffff;
    --soft-white: #e8f3fa;
    --portrait-border: #4a4a4a;
    --portrait-tone: #8a7a6e;
    --portrait-sepia: #c9b8a3;
    --badge-tone: #f2f2f2;
  }
  * { box-sizing: border-box; margin: 0; padding: 0; }
  html, body { width: 1200px; height: 675px; overflow: hidden; }
  body { font-family: "Arimo", Arial, sans-serif; color: var(--white); }
  .slide {
    position: relative; width: 1200px; height: 675px; overflow: hidden;
    background: linear-gradient(180deg, var(--sky-top) 0%, #3fa8da 55%, var(--sky-bottom) 100%);
  }
  .slide-title {
    position: absolute; left: 106px; top: 24px;
    font-family: "Poppins", "Century Gothic", sans-serif; font-weight: 600;
    font-size: 37px; letter-spacing: 0.5px; text-transform: uppercase;
  }
  .accent-lines { position: absolute; right: 0; top: 280px; }
  .portrait {
    position: absolute; border-radius: 50%;
    border: 2px solid var(--portrait-border);
    background: radial-gradient(circle at 50% 40%, #d9c2b0 0%, var(--portrait-tone) 60%, #3b3b3b 100%);
  }
  .portrait--lead { width: 104px; height: 104px; top: 104px; }
  .portrait--staff {
    width: 90px; height: 90px; top: 485px;
    background: radial-gradient(circle at 50% 40%, #efe4d6 0%, var(--portrait-sepia) 55%, #6e6254 100%);
  }
  .board-card {
    position: absolute; top: 213px; width: 277px; height: 244px;
    background: linear-gradient(180deg, var(--card-top) 0%, rgba(16,60,120,0.55) 35%, var(--card-bottom) 100%);
  }
  .board-card__name { position: absolute; left: 19px; top: 12px; font-weight: 700; font-size: 17px; }
  .board-card__degrees { position: absolute; left: 19px; top: 33px; font-style: italic; font-size: 10.5px; color: var(--soft-white); }
  .board-card__role { position: absolute; left: 19px; top: 47px; font-size: 18px; font-weight: 400; letter-spacing: 0.2px; }
  .affiliation { position: absolute; left: 12px; display: flex; align-items: center; }
  .affiliation__mark { width: 39px; height: 39px; background: var(--badge-tone); flex: none; }
  .affiliation__text { margin-left: 22px; font-size: 13.5px; line-height: 1.2; }
  .staff-member { position: absolute; top: 583px; }
  .staff-member__name { font-weight: 700; font-size: 17px; }
  .staff-member__role { font-size: 17px; margin-top: 2px; }
</style>
</head>
<body>
<main class="slide">
  <h1 class="slide-title">Team of experienced entrepreneurs</h1>

  <svg class="accent-lines" width="200" height="340" viewBox="0 0 200 340" aria-hidden="true">
    <g stroke="#ffffff" fill="none">
      <line x1="200" y1="10" x2="95" y2="130" stroke-width="1.2" opacity="0.8"/>
      <line x1="200" y1="40" x2="120" y2="130" stroke-width="1.2" opacity="0.8"/>
      <line x1="200" y1="70" x2="75" y2="210" stroke-width="1.2" opacity="0.8"/>
      <line x1="200" y1="75" x2="95" y2="195" stroke-width="3"/>
      <line x1="170" y1="140" x2="30" y2="300" stroke-width="1" opacity="0.7"/>
    </g>
  </svg>

  <div class="portrait portrait--lead" style="left:103px" role="img" aria-label="Portrait photo of Lena Hartwig"></div>
  <div class="portrait portrait--lead" style="left:455px" role="img" aria-label="Portrait photo of Daria Keller"></div>
  <div class="portrait portrait--lead" style="left:816px" role="img" aria-label="Portrait photo of Tobias Renner"></div>

  <section class="board-card" style="left:105px">
    <h2 class="board-card__name">Lena Hartwig</h2>
    <p class="board-card__degrees">MBA Uni Aarburg / Mesa Ridge State Univ.</p>
    <p class="board-card__role">Executive Director</p>
    <div class="affiliation" style="top:87px"><span class="affiliation__mark"></span><span class="affiliation__text">Veltrion,<br>Head Business Development</span></div>
    <div class="affiliation" style="top:135px"><span class="affiliation__mark"></span><span class="affiliation__text">Craftlane,<br>COO</span></div>
    <div class="affiliation" style="top:182px"><span class="affiliation__mark"></span><span class="affiliation__text">Halden Assurance,<br>Division Lead Innovation</span></div>
  </section>

  <section class="board-card" style="left:457px">
    <h2 class="board-card__name">Daria Keller</h2>
    <p class="board-card__degrees">MBA Uni Aarburg, Dipl. Teacher Uni Seeland</p>
    <p class="board-card__role">Supervisory Board</p>
    <div class="affiliation" style="top:87px"><span class="affiliation__mark"></span><span class="affiliation__text">Youthbridge,<br>Head Fundraising &amp; partnerships</span></div>
    <div class="affiliation" style="top:135px"><span class="affiliation__mark"></span><span class="affiliation__text">Lendloop,<br>Member of BoD</span></div>
    <div class="affiliation" style="top:182px"><span class="affiliation__mark"></span><span class="affiliation__text">Halden Assurance,<br>Chief of Staff / Member<br>of Senior Management</span></div>
  </section>

  <section class="board-card" style="left:818px">
    <h2 class="board-card__name">Tobias Renner</h2>
    <p class="board-card__degrees">PhD THR, MBA IBSF, MSc UNK</p>
    <p class="board-card__role">Supervisory Board</p>
    <div class="affiliation" style="top:87px"><span class="affiliation__mark"></span><span class="affiliation__text">Crumb Bar<br>Co-Founder, Chairman</span></div>
    <div class="affiliation" style="top:135px"><span class="affiliation__mark"></span><span class="affiliation__text">Lakeside Innovation Hub<br>(Aarwil) CEO</span></div>
    <div class="affiliation" style="top:182px"><span class="affiliation__mark"></span><span class="affiliation__text">Pedalo Mobility Inc.<br>Co-Founder, CEO</span></div>
  </section>

  <div class="portrait portrait--staff" style="left:105px" role="img" aria-label="Portrait photo of Marco Bellini"></div>
  <div class="portrait portrait--staff" style="left:385px" role="img" aria-label="Portrait photo of Nina Forster"></div>
  <div class="portrait portrait--staff" style="left:634px" role="img" aria-label="Portrait photo of Urs Lindt"></div>
  <div class="portrait portrait--staff" style="left:896px" role="img" aria-label="Portrait photo of Claire Dumont"></div>

  <div class="staff-member" style="left:105px"><p class="staff-member__name">Marco Bellini</p><p class="staff-member__role">Stores &amp; Corp. Services</p></div>
  <div class="staff-member" style="left:386px"><p class="staff-member__name">Nina Forster</p><p class="staff-member__role">Event Delivery</p></div>
  <div class="staff-member" style="left:638px"><p class="staff-member__name">Urs Lindt</p><p class="staff-member__role">Design &amp; Web-Shop</p></div>
  <div class="staff-member" style="left:908px"><p class="staff-member__name">Claire Dumont</p><p class="staff-member__role">Business Development</p></div>
</main>
</body>
</html>
```